We would like a business card that includes our logo on the front and the following information on the back:

Marcus Keene, Owner
Phone: (555) 614-8027
email: mkeenefencing@postvale.net

Marty Keene & Sons Fencing provides the following services:
Barbed wire
Smooth wire
High tensile
Electric

On the bottom of the card please add:
Please call or email Marcus for estimates.

```html
<!DOCTYPE html>
<html lang="en">
<head>
<meta charset="utf-8">
<title>Marty Keene &amp; Sons Fencing – Business Card</title>
<link href="https://fonts.googleapis.com/css2?family=Lato:ital,wght@0,300;0,400;0,700;1,300&display=swap" rel="stylesheet">
<style>
  :root {
    --backdrop: #1c1c1c;
    --paper: #ffffff;
    --brown: #7d5a40;
    --ink: #2b2b2b;
    --rule: #8a8a8a;
  }
  * { box-sizing: border-box; margin: 0; padding: 0; }
  html, body {
    width: 1200px; height: 958px; overflow: hidden;
    background: var(--backdrop);
    font-family: "Lato", sans-serif;
  }
  .sheet {
    width: 1200px; height: 958px;
    display: flex; flex-direction: column;
    align-items: center; justify-content: center; gap: 60px;
  }
  .card {
    position: relative;
    width: 630px; height: 360px;
    background: var(--paper);
    overflow: hidden;
  }

  /* Front */
  .card-front {
    display: flex; align-items: center; justify-content: center;
  }
  .front-lockup {
    display: flex; align-items: center; gap: 22px;
    color: var(--ink);
  }
  .front-lockup .mark {
    width: 26px; height: 26px; background: var(--ink); flex: none;
  }
  .front-name {
    font-size: 30px; font-weight: 400;
    letter-spacing: 0.08em; line-height: 1.35;
    text-transform: uppercase; text-align: center;
  }
  .front-name span { display: block; }

  /* Back */
  .contact {
    position: absolute; left: 48px; top: 92px;
    display: flex; align-items: center;
    white-space: nowrap;
  }
  .person { text-align: right; padding-right: 20px; }
  .person-name {
    color: var(--brown);
    font-size: 30px; font-weight: 400;
    text-transform: uppercase; line-height: 1;
  }
  .person-role {
    color: var(--ink); font-size: 15px; font-weight: 400; margin-top: 5px;
  }
  .divider { width: 1px; height: 66px; background: var(--rule); flex: none; }
  .details { padding-left: 18px; }
  .detail {
    display: flex; align-items: center; gap: 9px;
    color: var(--ink); font-size: 17px; font-weight: 300; line-height: 1.55;
  }
  .detail svg { width: 14px; height: 14px; flex: none; }

  .estimate-note {
    position: absolute; left: 48px; top: 212px;
    font-size: 14px; font-style: italic; font-weight: 300; color: var(--ink);
    white-space: nowrap;
  }
  .estimate-note .who { color: var(--brown); }

  .brand-tag {
    position: absolute; right: 24px; top: 36px;
    display: flex; align-items: center; gap: 7px;
    color: var(--brown); font-size: 11px; font-weight: 400;
    letter-spacing: 0.05em; text-transform: uppercase; white-space: nowrap;
  }
  .brand-tag .mark { width: 9px; height: 9px; background: var(--brown); }

  .services {
    position: absolute; left: 0; right: 0; bottom: 0; height: 56px;
    background: var(--brown); list-style: none;
    display: flex; align-items: center; justify-content: center; gap: 8px;
    color: var(--paper); font-size: 16px; letter-spacing: 0.02em;
    text-transform: uppercase; white-space: nowrap;
  }
  .services li { display: flex; align-items: center; gap: 8px; }
  .services svg { width: 12px; height: 12px; }
</style>
</head>
<body>
<main class="sheet">

  <section class="card card-front" aria-label="Card front">
    <div class="front-lockup">
      <span class="mark" aria-hidden="true"></span>
      <p class="front-name"><span>Marty Keene &amp; Sons</span><span>Fencing</span></p>
    </div>
  </section>

  <section class="card card-back" aria-label="Card back">
    <p class="brand-tag"><span class="mark" aria-hidden="true"></span>Marty Keene &amp; Sons Fencing</p>

    <div class="contact">
      <div class="person">
        <p class="person-name">Marcus Keene</p>
        <p class="person-role">Owner</p>
      </div>
      <span class="divider" aria-hidden="true"></span>
      <div class="details">
        <p class="detail">
          <svg viewBox="0 0 16 16" aria-hidden="true"><circle cx="8" cy="8" r="8" fill="var(--brown)"/><path d="M5.2 4.2l1.6 1.6-0.9 1.2c0.6 1.2 1.6 2.2 2.8 2.8l1.2-0.9 1.6 1.6-1 1.2c-2.9-0.5-5.2-2.8-5.7-5.7z" fill="#fff"/></svg>
          (555) 614-8027
        </p>
        <p class="detail">
          <svg viewBox="0 0 16 16" aria-hidden="true"><rect x="1" y="3.5" width="14" height="9" fill="var(--brown)"/><path d="M1.5 4l6.5 5 6.5-5" fill="none" stroke="#fff" stroke-width="1.1"/></svg>
          mkeenefencing@postvale.net
        </p>
      </div>
    </div>

    <p class="estimate-note">Please call or email <span class="who">Marcus</span> for estimates.</p>

    <ul class="services" aria-label="Services">
      <li>Barbed Wire<svg viewBox="0 0 12 12" aria-hidden="true"><circle cx="6" cy="6" r="6" fill="#fff"/><path d="M3.2 6.2l1.9 1.8 3.7-3.9" fill="none" stroke="var(--brown)" stroke-width="1.4"/></svg></li>
      <li>Smooth Wire<svg viewBox="0 0 12 12" aria-hidden="true"><circle cx="6" cy="6" r="6" fill="#fff"/><path d="M3.2 6.2l1.9 1.8 3.7-3.9" fill="none" stroke="var(--brown)" stroke-width="1.4"/></svg></li>
      <li>High Tensile<svg viewBox="0 0 12 12" aria-hidden="true"><circle cx="6" cy="6" r="6" fill="#fff"/><path d="M3.2 6.2l1.9 1.8 3.7-3.9" fill="none" stroke="var(--brown)" stroke-width="1.4"/></svg></li>
      <li>Electric</li>
    </ul>
  </section>

</main>
</body>
</html>
```